Design an App that allows to send money through messages

We need a design for an app that will be a text message app that allows you to send money in the messages.

This app is ChatterBox and CoinPouch infused into one app
CoinPouch - https://vidbay.example/k7QpRtZ2mWx

It also is a Crypto wallet, trade, buy, sell, swap, etc. I have attached a similar 'app' design however it needs to have it's own colour scheme.

Design an app similar to ChatterBox/Parleyo that allows to communicate with your contacts but also a Crypto wallet. In the actual messages users will be able to send Crypto tokens to each other - similar to qText Pear Pay (attached).

Design buttons, fields, wallet, and everything in the attached diagram of the other app.

These pages must be designed for the app:
- Login page (Login with phone number, pear ID)
- Main chats page (with all your messages with contacts)
- Actual messages (with the send money feature in a message - like pear pay)
- Crypto Wallet(s) with all tokens and assets
- Crypto Wallet import / new wallet page
- Buy/Sell Crypto token
- Markets page (shows all tokens - tokenboardly.com)
- Send/Receive pop-up
- Chart page of markets
- All transactions page
- Contacts page (from phone)
- Settings page (similar to chatterbox)

How payments will be made (via message):
https://vidbay.example/b3NfLxQ8sYe?t=77

Ideally design in Figma or other app for developers to understand which page is connected to which button.

Here is some inspiration on redesign chatterbox design app:
https://www.pinvault.example/pin/482716093527164839/

Winner who does all pages with the proper theme will receive an extra tip.

Payments through Messages and Cryptocurrency Buy/Sell/Trade/Swap/Send/Receive

Other font styles liked:
• Montserrat (or ANY font of your choosing)

• All App pages with Wireframe (Figma or Adobe XD)
• Creative designs throughout pages of app. Not your typical app.

```html
<!DOCTYPE html>
<html lang="en">
<head>
<meta charset="utf-8">
<title>Contacts</title>
<link rel="stylesheet" href="https://fonts.googleapis.com/css2?family=Nunito+Sans:wght@400;600;700;800&display=swap">
<style>
:root{
  --page:#eef1f4;
  --card:#ffffff;
  --header:#f7f9fc;
  --ink:#0d0f1c;
  --muted:#9a9ca3;
  --blue:#4ea4e8;
  --blue-soft:#e6f1fb;
  --line:#eceef1;
  --green:#3fd45b;
  --amber:#f5b21f;
  --pink-soft:#fbe6f3;
  --pink:#d85bb3;
}
*{box-sizing:border-box;margin:0;padding:0}
html,body{width:1064px;height:1200px;overflow:hidden}
body{background:var(--page);font-family:"Nunito Sans",Arial,sans-serif;color:var(--ink);position:relative}
.phone-screen{position:absolute;left:230px;top:44px;width:528px;height:1134px;background:var(--header);border-radius:28px;overflow:hidden}
.screen-title{position:absolute;left:53px;top:88px;font-size:25px;font-weight:800;letter-spacing:-.2px}
.round-btn{position:absolute;width:72px;height:72px;border-radius:50%;display:flex;align-items:center;justify-content:center}
.round-btn.swap{left:275px;top:68px;background:var(--blue-soft)}
.round-btn.add{left:362px;top:68px;background:var(--blue)}
.more{position:absolute;left:468px;top:90px}
.tabs{position:absolute;left:0;top:210px;width:100%;height:40px}
.tab{position:absolute;top:0;font-size:21px;color:var(--muted)}
.tab.active{color:var(--ink);font-weight:800}
.tab-underline{position:absolute;left:45px;top:37px;width:108px;height:4px;border-radius:2px;background:var(--blue)}
.list-panel{position:absolute;left:0;top:250px;width:100%;height:884px;background:var(--card);border-radius:22px 22px 0 0}
.section-badge{position:absolute;left:25px;width:25px;height:25px;border-radius:6px;background:var(--blue);color:#fff;font-size:14px;font-weight:700;display:flex;align-items:center;justify-content:center}
.section-rule{position:absolute;left:75px;width:384px;height:1px;background:#c9cbd0}
.alpha-index{position:absolute;left:476px;top:25px;width:24px;list-style:none}
.alpha-index li{height:25px;line-height:25px;text-align:center;font-size:17px;color:#9ea0a6}
.alpha-index li.current{background:var(--blue-soft);color:var(--blue);border-radius:5px}
.contact{position:absolute;left:0;width:100%;height:0}
.avatar{position:absolute;left:45px;top:-36px;width:72px;height:72px;border-radius:50%;display:flex;align-items:center;justify-content:center;font-size:22px;font-weight:600}
.avatar.initials-blue{background:var(--blue);color:#fff}
.avatar.initials-pink{background:var(--pink-soft);color:var(--pink)}
.status{position:absolute;left:97px;top:14px;width:20px;height:20px;border-radius:50%;border:3px solid #fff}
.status.online{background:var(--green)}
.status.away{background:var(--amber);display:flex;align-items:center;justify-content:center}
.name{position:absolute;left:158px;top:-32px;font-size:23px;font-weight:400;white-space:nowrap}
.preview{position:absolute;left:158px;top:3px;font-size:19px;color:var(--muted);white-space:nowrap;display:flex;align-items:center;gap:12px}
.time{position:absolute;right:63px;top:-24px;font-size:17px;color:var(--muted)}
.divider{position:absolute;left:134px;width:324px;height:1px;background:var(--line)}
.list-fade{position:absolute;left:0;top:700px;width:100%;height:56px;background:linear-gradient(rgba(255,255,255,0),#f1f2f4)}
.bottom-nav{position:absolute;left:0;top:1006px;width:100%;height:128px;background:var(--card);box-shadow:0 -8px 20px rgba(0,0,0,.05)}
.nav-icon{position:absolute;top:44px}
.send-btn{position:absolute;left:203px;top:34px;width:134px;height:57px;border-radius:14px;background:var(--blue);color:#fff;font-size:23px;font-weight:700;display:flex;align-items:center;justify-content:center}
.nav-dot{position:absolute;left:385px;top:92px;width:8px;height:8px;border-radius:50%;background:var(--blue)}
</style>
</head>
<body>
<main class="phone-screen">
  <h1 class="screen-title">Contacts</h1>
  <div class="round-btn swap" aria-label="Transfer">
    <svg width="32" height="32" viewBox="0 0 32 32" fill="none" stroke="#4ea4e8" stroke-width="2.4" stroke-linecap="round" stroke-linejoin="round"><path d="M5 11h21M21 5l6 6-6 6"/><path d="M27 22H6M11 16l-6 6 6 6"/></svg>
  </div>
  <div class="round-btn add" aria-label="Add contact">
    <svg width="30" height="30" viewBox="0 0 30 30" stroke="#fff" stroke-width="3" stroke-linecap="round"><path d="M15 4v22M4 15h22"/></svg>
  </div>
  <svg class="more" width="10" height="28" viewBox="0 0 10 28" fill="#0d0f1c"><circle cx="5" cy="4" r="2.6"/><circle cx="5" cy="14" r="2.6"/><circle cx="5" cy="24" r="2.6"/></svg>

  <nav class="tabs">
    <span class="tab active" style="left:65px">People</span>
    <span class="tab" style="left:204px">History</span>
    <span class="tab" style="left:342px">Sent</span>
    <span class="tab-underline"></span>
  </nav>

  <section class="list-panel">
    <span class="section-badge" style="top:25px">A</span>
    <ol class="alpha-index">
      <li class="current">A</li><li>B</li><li>C</li><li>D</li><li>E</li><li>F</li><li>G</li><li>H</li><li>I</li><li>J</li><li>K</li><li>L</li><li>M</li><li>N</li><li>O</li><li>P</li><li>R</li><li>Q</li><li>S</li><li>T</li><li>U</li><li>V</li><li>W</li><li>X</li><li>Y</li><li>Z</li>
    </ol>

    <div class="contact" style="top:108px">
      <div class="avatar" role="img" aria-label="Profile photo of Idris Mallory" style="background:linear-gradient(135deg,#b9bcc2,#7d7f86)"></div>
      <span class="status online"></span>
      <span class="name">Idris Mallory</span>
      <span class="preview">120 ETH <svg width="18" height="14" viewBox="0 0 18 14" fill="none" stroke="#0d0f1c" stroke-width="2" stroke-linecap="round" stroke-linejoin="round"><path d="M2 7l5 5L16 2"/></svg></span>
      <span class="time">2 min ago</span>
    </div>
    <span class="divider" style="top:167px"></span>

    <div class="contact" style="top:220px">
      <div class="avatar initials-blue">MV</div>
      <span class="status away"><svg width="10" height="10" viewBox="0 0 10 10" fill="none" stroke="#fff" stroke-width="1.6"><circle cx="5" cy="5" r="4"/><path d="M5 2.5V5l1.6 1"/></svg></span>
      <span class="name">Milo Varden</span>
      <span class="preview">This is a test for view <svg width="18" height="14" viewBox="0 0 18 14" fill="none" stroke="#0d0f1c" stroke-width="2" stroke-linecap="round" stroke-linejoin="round"><path d="M2 7l5 5L16 2"/></svg></span>
      <span class="time">12/5/2022</span>
    </div>
    <span class="divider" style="top:278px"></span>

    <div class="contact" style="top:334px">
      <div class="avatar initials-pink">CC</div>
      <span class="name">Craft Circle</span>
      <span class="preview">This is a test message...</span>
      <span class="time">12/5/2022</span>
    </div>
    <span class="divider" style="top:394px"></span>

    <div class="contact" style="top:445px">
      <div class="avatar" role="img" aria-label="Profile photo of Jonah Reede" style="background:linear-gradient(135deg,#e2b43a,#b56a3c)"></div>
      <span class="name">Jonah Reede</span>
      <span class="preview">Any other changes...</span>
      <span class="time">12/3/2022</span>
    </div>

    <span class="section-badge" style="top:499px">B</span>
    <span class="section-rule" style="top:511px"></span>

    <div class="contact" style="top:577px">
      <div class="avatar" role="img" aria-label="Profile photo of Clara Devlin" style="background:linear-gradient(135deg,#3c5a3a,#1f2a22)"></div>
      <span class="name">Clara Devlin</span>
      <span class="preview">Sent 0.345268 BTC <svg width="16" height="16" viewBox="0 0 16 16" stroke="#0d0f1c" stroke-width="2" stroke-linecap="round"><path d="M3 3l10 10M13 3L3 13"/></svg></span>
      <span class="time">11/3/2022</span>
    </div>
    <span class="divider" style="top:637px"></span>

    <div class="contact" style="top:689px">
      <div class="avatar" role="img" aria-label="Profile photo of Jonah Reede" style="background:linear-gradient(135deg,#c4213b,#241a3a)"></div>
      <span class="name">Jonah Reede</span>
      <span class="preview">This is a test for view</span>
      <span class="time">11/3/2022</span>
    </div>
    <div class="list-fade"></div>
  </section>

  <nav class="bottom-nav">
    <svg class="nav-icon" style="left:48px" width="36" height="34" viewBox="0 0 36 34" fill="none" stroke="#0d0f1c" stroke-width="2.6" stroke-linecap="round"><path d="M3 3v28h30"/><path d="M10 24v-8M16 24v-5M22 24v-11M28 24V7"/></svg>
    <svg class="nav-icon" style="left:132px;top:46px" width="36" height="30" viewBox="0 0 36 30" fill="none" stroke="#0d0f1c" stroke-width="2.6" stroke-linejoin="round"><rect x="2" y="3" width="31" height="24" rx="5"/><path d="M33 11h-9a4 4 0 0 0 0 8h9"/></svg>
    <div class="send-btn">Send</div>
    <svg class="nav-icon" style="left:372px;top:40px" width="34" height="40" viewBox="0 0 34 40" fill="none" stroke="#4ea4e8" stroke-width="2.6"><circle cx="17" cy="11" r="8"/><path d="M3 37c0-8 6-13 14-13s14 5 14 13z" stroke-linejoin="round"/></svg>
    <span class="nav-dot"></span>
    <svg class="nav-icon" style="left:447px;top:43px" width="36" height="36" viewBox="0 0 24 24" fill="none" stroke="#0d0f1c" stroke-width="1.8" stroke-linecap="round" stroke-linejoin="round"><circle cx="12" cy="12" r="3"/><path d="M19.4 15a1.7 1.7 0 0 0 .3 1.8l.1.1a2 2 0 1 1-2.8 2.8l-.1-.1a1.7 1.7 0 0 0-1.8-.3 1.7 1.7 0 0 0-1 1.5V21a2 2 0 1 1-4 0v-.1a1.7 1.7 0 0 0-1.1-1.5 1.7 1.7 0 0 0-1.8.3l-.1.1a2 2 0 1 1-2.8-2.8l.1-.1a1.7 1.7 0 0 0 .3-1.8 1.7 1.7 0 0 0-1.5-1H3a2 2 0 1 1 0-4h.1a1.7 1.7 0 0 0 1.5-1.1 1.7 1.7 0 0 0-.3-1.8l-.1-.1a2 2 0 1 1 2.8-2.8l.1.1a1.7 1.7 0 0 0 1.8.3H9a1.7 1.7 0 0 0 1-1.5V3a2 2 0 1 1 4 0v.1a1.7 1.7 0 0 0 1 1.5 1.7 1.7 0 0 0 1.8-.3l.1-.1a2 2 0 1 1 2.8 2.8l-.1.1a1.7 1.7 0 0 0-.3 1.8V9a1.7 1.7 0 0 0 1.5 1H21a2 2 0 1 1 0 4h-.1a1.7 1.7 0 0 0-1.5 1z"/></svg>
  </nav>
</main>
</body>
</html>
```